Bus. Card/Envelope/Letterhead Design Request with my Logo

I have a logo created. I need to create a business card design, letterhead design and envelope design with the new logo.
Updates

The logo has now been posted. Thank you.

Target Market(s)

Professional. Legal Field.

Industry/Entity Type

Business

Requirements
Must have
• I like the same font as the logo.

```html
<!DOCTYPE html>
<html lang="en">
<head>
<meta charset="utf-8">
<title>Marlowe Quinn LLP – Business Card</title>
<link rel="stylesheet" href="https://fonts.googleapis.com/css2?family=Cinzel:wght@400;700&family=Open+Sans:wght@400;600&display=swap">
<style>
  :root {
    --backdrop: #ececec;
    --card: #ffffff;
    --ink: #3a3a3a;
    --ink-soft: #6b6b6b;
    --rule: #4a4a4a;
    --leaf: #7ea83a;
    --spectrum: linear-gradient(90deg,
      #e23b3b 0%, #f0a23a 12%, #d9c92a 20%, #5fb63b 32%, #3bab5a 44%,
      #2fb3c9 54%, #3a6fd0 64%, #3b3f9e 74%, #6a3aa8 84%, #c2388f 92%, #e02a2a 100%);
    --spectrum-v: linear-gradient(180deg,
      #e23b3b 0%, #f0a23a 12%, #d9c92a 20%, #5fb63b 32%, #3bab5a 44%,
      #2fb3c9 54%, #3a6fd0 64%, #3b3f9e 74%, #6a3aa8 84%, #c2388f 92%, #e02a2a 100%);
  }
  * { margin: 0; padding: 0; box-sizing: border-box; }
  html, body { width: 1200px; height: 1015px; overflow: hidden; background: var(--backdrop); }
  .stage { position: relative; width: 1200px; height: 1015px; }

  .card {
    position: absolute; top: 357px; width: 520px; height: 300px;
    background: var(--card); overflow: hidden;
    box-shadow: 0 6px 18px rgba(0,0,0,.12);
  }
  .card--front { left: 50px; }
  .card--back { left: 630px; }

  .firm-name {
    font-family: "Cinzel", serif; font-size: 21px; letter-spacing: 1px;
    color: var(--ink); white-space: nowrap;
  }
  .firm-mark { display: inline-block; width: 12px; height: 12px; border-radius: 50%; background: var(--leaf); margin-left: 8px; vertical-align: middle; }
  .firm-tagline {
    display: flex; align-items: center; gap: 8px; margin-top: 6px;
    font-family: "Cinzel", serif; font-size: 8px; letter-spacing: 3px; color: var(--ink-soft);
  }
  .firm-tagline::before, .firm-tagline::after { content: ""; width: 22px; height: 1px; background: var(--ink-soft); }
  .firm-block { border-top: 2px solid var(--rule); border-bottom: 1px solid var(--rule); padding: 7px 2px 8px; display: inline-block; }

  .front__brand { position: absolute; left: 30px; top: 26px; }
  .person { position: absolute; left: 30px; top: 122px; padding-left: 20px; }
  .person::before {
    content: ""; position: absolute; left: 0; top: 3px;
    border-left: 11px solid var(--leaf); border-top: 7px solid transparent; border-bottom: 7px solid transparent;
  }
  .person__name { font-family: "Cinzel", serif; font-weight: 700; font-size: 15px; color: var(--ink); letter-spacing: .5px; }
  .person__role { font-family: "Open Sans", sans-serif; font-size: 11px; color: var(--ink-soft); margin-top: 2px; }

  .divider { position: absolute; left: 262px; top: 112px; width: 1px; height: 110px; background: #9a9a9a; }

  .contacts { position: absolute; left: 280px; top: 104px; list-style: none; font-family: "Open Sans", sans-serif; font-size: 10.5px; color: var(--ink); }
  .contacts li { display: flex; align-items: center; gap: 9px; margin-bottom: 7px; line-height: 1.3; }
  .contacts svg { flex: none; width: 22px; height: 22px; }

  .spectrum-band { position: absolute; left: 0; right: 0; bottom: 0; height: 58px; background: var(--spectrum); }

  .back__band {
    position: absolute; left: 70px; top: 0; bottom: 0; width: 380px;
    background: var(--spectrum);
    display: flex; align-items: center; justify-content: center;
  }
  .back__band .firm-block { border-color: #2e2e2e; }
  .back__band .firm-name, .back__band .firm-tagline { color: #2e2e2e; }
  .back__band .firm-tagline::before, .back__band .firm-tagline::after { background: #2e2e2e; }
</style>
</head>
<body>
<main class="stage">

  <section class="card card--front" aria-label="Business card front">
    <div class="front__brand">
      <div class="firm-block">
        <div class="firm-name">Marlowe Quinn LLP<span class="firm-mark"></span></div>
        <div class="firm-tagline">ATTORNEYS AT LAW</div>
      </div>
    </div>

    <div class="person">
      <div class="person__name">DANIEL REYES</div>
      <div class="person__role">Managing Director</div>
    </div>

    <div class="divider"></div>

    <ul class="contacts">
      <li>
        <svg viewBox="0 0 22 22" aria-hidden="true"><circle cx="11" cy="11" r="11" fill="#7ea83a"/><path d="M7 6.5c.6-.6 1.4-.5 1.8.1l1 1.5c.3.5.2 1-.2 1.4l-.6.5c.6 1.3 1.6 2.3 2.9 2.9l.5-.6c.4-.4.9-.5 1.4-.2l1.5 1c.6.4.7 1.2.1 1.8-2.5 2.4-10.8-5.9-8.4-8.4z" fill="#fff"/></svg>
        <span>555 210 4471<br>555 210 4472</span>
      </li>
      <li>
        <svg viewBox="0 0 22 22" aria-hidden="true"><circle cx="11" cy="11" r="11" fill="#7ea83a"/><rect x="5.5" y="7" width="11" height="8" rx="1" fill="none" stroke="#fff" stroke-width="1.4"/><path d="M5.8 7.5 11 11.5l5.2-4" fill="none" stroke="#fff" stroke-width="1.4"/></svg>
        <span>d.reyes@marlowequinn.com</span>
      </li>
      <li>
        <svg viewBox="0 0 22 22" aria-hidden="true"><circle cx="11" cy="11" r="11" fill="#7ea83a"/><rect x="7.5" y="5.5" width="7" height="11" rx="1.2" fill="none" stroke="#fff" stroke-width="1.4"/></svg>
        <span>www.marlowequinn.com</span>
      </li>
      <li>
        <svg viewBox="0 0 22 22" aria-hidden="true"><circle cx="11" cy="11" r="11" fill="#7ea83a"/><path d="M11 17s-4-4.2-4-7a4 4 0 0 1 8 0c0 2.8-4 7-4 7z" fill="#fff"/><circle cx="11" cy="10" r="1.5" fill="#7ea83a"/></svg>
        <span>88 Cedar Avenue,<br>Suite 410 Brookfield,<br>Ohio 44403</span>
      </li>
    </ul>

    <div class="spectrum-band"></div>
  </section>

  <section class="card card--back" aria-label="Business card back">
    <div class="back__band">
      <div class="firm-block">
        <div class="firm-name">Marlowe Quinn LLP<span class="firm-mark"></span></div>
        <div class="firm-tagline">ATTORNEYS AT LAW</div>
      </div>
    </div>
  </section>

</main>
</body>
</html>
```